Redesign of Brochure of company services

We need a redesign a brochure. All of the content on the existing brochure correct, but the design we are not pleased with it. I will provide the previous brochure. Every Window Bright is Angolan company that provides multiple service ranging providing fruits, vegetables, fisheries, and meat to multiple industries in angola. Every Window Bright seeks to start delivering or providing their service to home owners looking for fresh products. We want a brochure design that covers all of these aspects.

Target Market(s)

Home owners, middle and upper age mothers, middle and upper class

Industry/Entity Type

Retail

Requirements
Must have
• Logo of the company and the content info
Nice to have
• It's up to you

```html
<!DOCTYPE html>
<html lang="pt">
<head>
<meta charset="utf-8">
<title>Every Window Bright Corporation – Brochura</title>
<link href="https://fonts.googleapis.com/css2?family=Questrial&family=Nunito+Sans:wght@600;700;800&display=swap" rel="stylesheet">
<style>
:root{
  --backdrop:#f1eedb;
  --paper:#ffffff;
  --green:#62a744;
  --orange:#f4862a;
  --red:#e84e27;
  --gold:#eeae22;
  --gold-light:#f6b92f;
  --gold-deep:#e9a41f;
  --ink:#1d1d1b;
  --ink-green:#2f5f2a;
}
*{margin:0;padding:0;box-sizing:border-box}
html,body{width:1200px;height:900px;overflow:hidden;background:var(--backdrop)}
body{position:relative;font-family:"Questrial",sans-serif;color:var(--ink)}
.sheet{position:absolute;left:226px;top:12px;width:749px;height:871px;background:var(--paper);overflow:hidden}
.abs{position:absolute}
.sun-arcs{position:absolute;left:0;top:0}
.hero{left:12px;top:13px;width:354px;height:166px;background:linear-gradient(#4f8fd6 0%,#a9d2f0 42%,#fdf2b0 50%,#7fbf3a 56%,#3f8a1f 100%)}
.hero-band{position:absolute;left:0;bottom:0;width:100%;height:32px;background:rgba(20,40,20,.45);color:#fff;font-size:17px;letter-spacing:.5px;text-align:right;padding:6px 20px 0 0}
.manager-head{left:12px;top:185px;width:354px;height:46px;background:var(--gold);font-family:"Nunito Sans",sans-serif;font-weight:700;font-size:17px;color:var(--ink);padding:12px 0 0 65px}
.manager-body{left:12px;top:237px;width:354px;height:104px;background:var(--gold-light)}
.portrait{left:23px;top:9px;width:80px;height:81px;background:linear-gradient(#d9b9a5,#8a5a44)}
.quote{left:113px;top:8px;width:210px;font-size:11.3px;line-height:13px;text-align:justify}
.signature{left:113px;top:71px;font-family:"Nunito Sans",sans-serif;font-weight:700;font-size:12.5px;color:var(--ink-green)}
.open-bar{left:12px;top:365px;width:354px;height:68px;background:var(--red);color:#fff;font-family:"Nunito Sans",sans-serif;font-weight:800;font-size:24px;padding:18px 0 0 21px;letter-spacing:.3px}
.contact{left:34px;font-size:18px;display:flex;align-items:center;gap:18px}
.producer-note{left:34px;top:561px;font-size:14px;line-height:18px}
.address-box{left:12px;top:675px;width:354px;height:116px;background:var(--green);color:#fff;font-family:"Nunito Sans",sans-serif;font-weight:700;padding:30px 0 0 131px}
.address-box .name{font-size:17px;line-height:20px}
.address-box .line{font-size:14px;line-height:17px}
.brand-title{left:403px;top:40px;font-size:35px;line-height:40px}
.brand-sub{left:403px;top:80px;font-family:"Nunito Sans",sans-serif;font-weight:700;font-size:20px;color:var(--red)}
.category{left:378px;width:259px;height:117px;color:#fff;font-size:18px;line-height:21px;padding-left:124px;display:flex;align-items:center}
.cat-veg{top:123px;background:var(--green)}
.cat-fruit{top:246px;background:var(--orange);padding-top:55px}
.cat-meat{top:369px;background:var(--red);padding-top:30px}
.produce{left:644px;width:105px;height:117px}
.ph-veg{top:123px;background:radial-gradient(circle at 40% 50%,#5f9a2a,#2f5a12 60%,#c23a1a)}
.ph-fruit{top:246px;background:radial-gradient(circle at 50% 60%,#e7c26a,#b85a28 55%,#7a3a1a)}
.ph-meat{top:369px;background:radial-gradient(circle at 60% 60%,#e07a55,#b3502f 50%,#8f9aa3)}
.brand-mark{left:387px;top:698px;width:236px;text-align:center;font-size:40px;line-height:46px;color:var(--ink)}
.tagline{left:387px;top:757px;width:236px;text-align:center;font-family:"Nunito Sans",sans-serif;font-weight:700;font-size:15px;line-height:19px}
</style>
</head>
<body>
<main class="sheet">
  <svg class="sun-arcs" width="749" height="871" aria-hidden="true">
    <circle cx="924" cy="188" r="280" fill="var(--gold-deep)"/>
    <circle cx="960" cy="188" r="270" fill="var(--gold-light)"/>
    <circle cx="924" cy="548" r="345" fill="var(--gold-deep)"/>
    <circle cx="965" cy="548" r="330" fill="var(--gold-light)"/>
    <rect x="560" y="489" width="200" height="4" fill="#fff"/>
    <rect x="560" y="611" width="200" height="4" fill="#fff"/>
    <rect x="560" y="733" width="200" height="4" fill="#fff"/>
  </svg>

  <div class="abs hero" role="img" aria-label="Foto de campo verde de cultivo sob céu azul com sol nascente">
    <div class="hero-band">Qualidade. Rapidez. Satisfação</div>
  </div>

  <div class="abs manager-head">Mensagem do gerente</div>
  <div class="abs manager-body">
    <div class="abs portrait" role="img" aria-label="Retrato da gerente"></div>
    <p class="abs quote">A nossa missão é aproximar os produtores nacionais dos seus clientes finais, garantindo qualidade e consistência.”</p>
    <p class="abs signature">Luzia Tavares - Gerente</p>
  </div>

  <div class="abs open-bar">ESTAMOS ABERTOS 24/24</div>

  <div class="abs contact" style="top:446px">
    <svg width="40" height="40" viewBox="0 0 40 40" aria-hidden="true">
      <circle cx="20" cy="20" r="17.5" fill="none" stroke="var(--ink)" stroke-width="2.5"/>
      <path d="M14 11c-2 1-3 3-2 6 2 6 6 10 12 12 3 1 5 0 6-2l-3-3-3 2c-3-1-6-4-7-7l2-3z" fill="var(--ink)"/>
    </svg>
    <span>+244 900 123 456</span>
  </div>
  <div class="abs contact" style="top:498px">
    <svg width="42" height="34" viewBox="0 0 42 34" aria-hidden="true">
      <path d="M3 9 35 3 39 25 7 31Z M3 9l19 11 13-17 M7 31l10-13 M39 25 25 16" fill="none" stroke="var(--ink)" stroke-width="2" stroke-linejoin="round"/>
    </svg>
    <span>luzia_tavares@example.com</span>
  </div>

  <p class="abs producer-note">Se for produtor e deseja comercializar os seus<br>produtos de forma segura, contacte-nos hoje!</p>

  <div class="abs address-box">
    <div class="name">Every Window Bright Corp</div>
    <div class="line">Estamos no Vila Nova</div>
    <div class="line">Luanda, Angola</div>
  </div>

  <h1 class="abs brand-title" style="font-weight:400">Every Window Bright</h1>
  <p class="abs brand-sub">Corporation</p>

  <div class="abs category cat-veg">Hortaliças</div>
  <div class="abs category cat-fruit">Frutas</div>
  <div class="abs category cat-meat">Carnes Peixes<br>Mariscos</div>

  <div class="abs produce ph-veg" role="img" aria-label="Foto de hortaliças frescas variadas"></div>
  <div class="abs produce ph-fruit" role="img" aria-label="Foto de frutas frescas variadas"></div>
  <div class="abs produce ph-meat" role="img" aria-label="Foto de peixe fresco"></div>

  <div class="abs brand-mark">ewbcorp</div>
  <p class="abs tagline">Levamos produtos frescos<br>Nacionais à sua porta</p>
</main>
</body>
</html>
```